US company needs luxury product packaging design for a line of hair extensions

What we Need:
Design product packaging for our top of the line hair extension product called Sorvanta™, the design should have the Sorvanta™ name,and the head from our Quillodor logo on the box.

Who we are
Our company QuilloDor™ is a wholesaler of 100% human hair extensions. We sell the best quality double drawn hair wefts, clip-ins and wigs.

The detailed brief is in the attached word document with examples of packaging we like and we have also uploaded our company logo

The winning designer(s) will work with us on 9 other products packages that we need, so it is important to think strategically

Thanks

Target Market(s)

African American Women

Industry/Entity Type

Hair And Beauty

Font styles to use
Serif
Decorative
Script

Colors
fbf289
b768aa
e24096
000000
fbd4d5
f59195
ffc214
d3a5cc
eda3c7

Requirements
Must have
• Evoke luxury
Nice to have
• See Attached brief

```html
<!DOCTYPE html>
<html lang="en">
<head>
<meta charset="utf-8">
<title>Velorine Drawer Slider Rigid Box – Dielines</title>
<link rel="stylesheet" href="https://fonts.googleapis.com/css2?family=Arimo&family=Playfair+Display:ital,wght@0,400;1,400&display=swap">
<style>
  :root {
    --bg: #b4b4b4;
    --ink: #111111;
    --purple: #5b0080;
    --purple-deep: #230039;
    --black: #050008;
    --gold: #e8b020;
    --blush: #fbd4d5;
    --white: #ffffff;
    --frame: #555555;
    --magenta: #d0155e;
  }
  html, body { margin: 0; padding: 0; overflow: hidden; }
  body { width: 1200px; height: 1200px; background: var(--bg); position: relative; }
  .spec-sheet {
    position: absolute; left: 23px; top: 240px;
    font-family: "Arimo", Arial, sans-serif; font-size: 10.5px; line-height: 13.5px; color: var(--ink);
    text-transform: uppercase;
  }
  .spec-sheet .spec-title { font-size: 12.5px; margin-bottom: 2px; }
  .spec-sheet .spec-url { text-transform: none; }
  .dielines { position: absolute; left: 0; top: 0; }
  .wordmark { font-family: "Playfair Display", Georgia, serif; font-weight: 400; font-style: normal; fill: var(--blush); }
  .tagline { font-family: "Playfair Display", Georgia, serif; font-style: italic; fill: var(--gold); }
  .small-copy { font-family: "Arimo", Arial, sans-serif; }
</style>
</head>
<body>
  <div class="spec-sheet">
    <div class="spec-title">Drawer Slider Rigid Box</div>
    <div>Customer: CLIENT4417 (GIGWORKS)</div>
    <div>CAD Drawing built by:</div>
    <div>DANA HOLLOWAY (<span class="spec-url">www.foldlinestudio.com</span>)</div>
    <div>Date revised: 15 Sept 2016</div>
    <div>Style: Custom Rigid Box</div>
    <div>Size: Drawer - 10" X 8" X 3"</div>
    <div>Sleeve - 10.125" X 3.125" X 8.125"</div>
    <div>Material: .060 Gauge Paperboard Thickness</div>
  </div>

  <svg class="dielines" width="1200" height="1200" viewBox="0 0 1200 1200">
    <defs>
      <linearGradient id="fade-vertical" x1="0" y1="0" x2="0" y2="1">
        <stop offset="0" stop-color="var(--black)"/>
        <stop offset="0.25" stop-color="var(--purple)"/>
        <stop offset="0.75" stop-color="var(--purple)"/>
        <stop offset="1" stop-color="var(--black)"/>
      </linearGradient>
      <linearGradient id="fade-left" x1="0" y1="0" x2="1" y2="0">
        <stop offset="0" stop-color="var(--black)"/>
        <stop offset="1" stop-color="var(--purple)"/>
      </linearGradient>
      <linearGradient id="fade-right" x1="1" y1="0" x2="0" y2="0">
        <stop offset="0" stop-color="var(--black)"/>
        <stop offset="1" stop-color="var(--purple)"/>
      </linearGradient>
      <linearGradient id="sleeve-fill" x1="0" y1="0" x2="0" y2="1">
        <stop offset="0" stop-color="#0a000f"/>
        <stop offset="0.55" stop-color="#2a0a40"/>
        <stop offset="1" stop-color="#4a1270"/>
      </linearGradient>
      <linearGradient id="flap-fill" x1="0" y1="0" x2="0" y2="1">
        <stop offset="0" stop-color="#0a000f"/>
        <stop offset="1" stop-color="#2a0a40"/>
      </linearGradient>
      <radialGradient id="portrait-fill" cx="0.5" cy="0.4" r="0.6">
        <stop offset="0" stop-color="#ff3a80"/>
        <stop offset="0.7" stop-color="var(--magenta)"/>
        <stop offset="1" stop-color="#7a0a45"/>
      </radialGradient>
    </defs>

    <!-- Drawer outer tray -->
    <g class="drawer-outer">
      <path d="M453 313 H631 V366 L636 375 V532 L631 540 V593 H453 V540 L448 532 V375 L453 366 Z" fill="url(#fade-vertical)"/>
      <path d="M384 366 H448 L453 376 V531 L448 540 H384 Z" fill="url(#fade-left)"/>
      <path d="M700 366 H636 L631 376 V531 L636 540 H700 Z" fill="url(#fade-right)"/>
    </g>

    <!-- Drawer liner -->
    <g class="drawer-liner">
      <rect x="826" y="333" width="178" height="240" fill="var(--white)"/>
      <rect x="826" y="333" width="178" height="25" fill="var(--purple-deep)"/>
      <rect x="826" y="548" width="178" height="25" fill="var(--purple-deep)"/>
      <rect x="777" y="382" width="49" height="142" fill="var(--white)"/>
      <rect x="777" y="382" width="24" height="142" fill="var(--purple-deep)"/>
      <rect x="1004" y="382" width="48" height="142" fill="var(--white)"/>
      <rect x="1028" y="382" width="24" height="142" fill="var(--purple-deep)"/>
      <rect x="828" y="384" width="174" height="138" rx="6" fill="var(--white)" stroke="var(--frame)" stroke-width="2"/>

      <g class="liner-promise small-copy" transform="rotate(180 915 410)" fill="#333" font-size="3.6" text-anchor="middle">
        <line x1="870" y1="392" x2="960" y2="392" stroke="#888" stroke-width="0.5"/>
        <text x="915" y="399" font-size="4">OUR PROMISE</text>
        <text x="915" y="407">Every Sorvanta™ piece is hand inspected</text>
        <text x="915" y="412">before it ships to you.</text>
        <line x1="870" y1="427" x2="960" y2="427" stroke="#888" stroke-width="0.5"/>
      </g>

      <g class="liner-about small-copy" fill="#333" font-size="3.6" text-anchor="middle">
        <text x="915" y="475" font-size="4">ABOUT SORVANTA</text>
        <line x1="870" y1="478" x2="960" y2="478" stroke="#888" stroke-width="0.5"/>
        <text x="915" y="485">Sorvanta™ is an ultra luxurious 100% human</text>
        <text x="915" y="490">hair line from Quillodor, made to be</text>
        <text x="915" y="495">colored, curled and styled</text>
        <text x="915" y="500">like your own.</text>
        <line x1="870" y1="512" x2="960" y2="512" stroke="#888" stroke-width="0.5"/>
      </g>
    </g>

    <!-- Sleeve -->
    <g class="sleeve">
      <rect x="113" y="675" width="180" height="56" fill="url(#flap-fill)"/>
      <path d="M61 715 H112 V890 H61 L58 878 V727 Z" fill="url(#sleeve-fill)"/>
      <path d="M112 731 L115 715 H291 L294 731 V874 L291 890 H115 L112 874 Z" fill="url(#sleeve-fill)"/>
      <path d="M294 731 L297 715 H345 L348 731 V874 L345 890 H297 L294 874 Z" fill="url(#sleeve-fill)"/>
      <path d="M348 731 L351 715 H523 L526 731 V874 L523 890 H351 L348 874 Z" fill="url(#sleeve-fill)"/>
      <path d="M526 731 L545 737 V868 L526 874 Z" fill="url(#sleeve-fill)"/>

      <!-- left side panel -->
      <g class="side-panel">
        <text class="wordmark" transform="translate(82 802) rotate(90)" font-size="18" text-anchor="middle">Velorine</text>
        <text class="tagline" transform="translate(72 802) rotate(90)" font-size="4.5" text-anchor="middle">100% Human Hair Extensions</text>
        <rect x="63" y="858" width="7" height="7" fill="#cfcfcf"/>
        <circle cx="101" cy="862" r="5" fill="#cfcfcf"/>
      </g>

      <!-- front panel -->
      <g class="front-panel">
        <path d="M205 734 C230 730 256 750 256 785 C256 812 238 830 212 832 C196 822 175 818 165 810 C172 795 172 780 170 768 C172 748 186 737 205 734 Z"
              fill="url(#portrait-fill)" role="img" aria-label="Illustrated profile of a woman with long flowing sparkling magenta hair"/>
        <text class="wordmark" x="205" y="847" font-size="16" text-anchor="middle">Velorine</text>
        <text class="tagline" x="205" y="856" font-size="4.5" text-anchor="middle">100% Human Hair Extensions</text>
        <line x1="155" y1="864" x2="255" y2="864" stroke="var(--gold)" stroke-width="0.6"/>
      </g>

      <!-- right side panel -->
      <g class="side-panel">
        <text class="wordmark" transform="translate(316 790) rotate(-90)" font-size="18" text-anchor="middle">Velorine</text>
        <text class="tagline" transform="translate(332 790) rotate(-90)" font-size="4.5" text-anchor="middle">100% Human Hair Extensions</text>
        <circle cx="303" cy="862" r="5" fill="#cfcfcf"/>
        <rect x="337" y="858" width="7" height="7" fill="#cfcfcf"/>
      </g>

      <!-- back panel -->
      <g class="back-panel">
        <rect x="351" y="733" width="174" height="139" fill="none" stroke="#5a3a70" stroke-width="0.6"/>
        <text class="wordmark" x="438" y="801" font-size="17" text-anchor="middle">Velorine</text>
        <text class="small-copy" x="438" y="809" font-size="3.6" fill="#cccccc" text-anchor="middle">100% HUMAN HAIR EXTENSIONS</text>
        <line x1="390" y1="843" x2="486" y2="843" stroke="#8a6aa0" stroke-width="0.5"/>
        <g class="small-copy" font-size="3.3" fill="#bbbbbb" text-anchor="middle">
          <text x="438" y="849">Product of Quillodor LLC. All rights reserved.</text>
          <text x="438" y="854">Velorine name and Quillodor are trademarks of Quillodor</text>
          <text x="438" y="859">LLC, registered in the USA.</text>
        </g>
        <line x1="390" y1="865" x2="486" y2="865" stroke="#8a6aa0" stroke-width="0.5"/>
      </g>
    </g>

    <!-- Sleeve liner blank -->
    <path class="sleeve-liner" d="M697 734 H753 V680 L755 666 H922 L924 680 V734 H1166 L1178 737 V867 L1166 870 H697 Z" fill="var(--white)"/>
  </svg>
</body>
</html>
```